lawn sign

Lawn Sign
Roofing Gutters Windows

Target Market(s)

roofing

Font styles to use
Sans Serif

Colors
86cfc6
33a6d7
fbee3f
faa54b

Requirements
Must have
• my logo
Nice to have
• designer for now

```html
<!DOCTYPE html>
<html lang="en">
<head>
<meta charset="utf-8">
<title>Harlow Restoration – Lawn Sign</title>
<link rel="stylesheet" href="https://fonts.googleapis.com/css2?family=Oswald:wght@400;700&display=swap">
<style>
  :root {
    --backdrop: #e6e6e6;
    --sign-white: #ffffff;
    --leaf-green: #84bc64;
    --forest-green: #0b914b;
    --sky-blue: #1e88c7;
    --rule-blue: #29a3dc;
    --service-green: #0f6b36;
    --name-teal: #128585;
    --bar-top: #1f86c6;
    --bar-bottom: #224a8e;
    --ink: #111111;
  }
  html, body {
    margin: 0;
    padding: 0;
    width: 1200px;
    height: 1200px;
    overflow: hidden;
    background: var(--backdrop);
  }
  .lawn-sign {
    position: absolute;
    left: 30px;
    top: 172px;
    width: 1140px;
    height: 855px;
    display: block;
  }
  .sign-face { fill: var(--sign-white); }
  .band-leaf { fill: var(--leaf-green); }
  .band-forest { fill: var(--forest-green); }
  .band-sky { fill: var(--sky-blue); }
  .company-name {
    font-family: "Oswald", sans-serif;
    font-weight: 400;
    fill: var(--name-teal);
    letter-spacing: 4px;
  }
  .divider { stroke: var(--rule-blue); stroke-width: 4; }
  .service {
    font-family: "Oswald", sans-serif;
    font-weight: 700;
    font-size: 125px;
    fill: var(--service-green);
  }
  .phone-ring { fill: none; stroke: var(--sign-white); stroke-width: 6; }
  .phone-glyph { fill: var(--sign-white); }
  .phone-number {
    font-family: "Oswald", sans-serif;
    font-weight: 700;
    font-size: 190px;
    fill: var(--sign-white);
  }
  .website {
    font-family: "Oswald", sans-serif;
    font-weight: 700;
    font-size: 88px;
    fill: var(--ink);
  }
</style>
</head>
<body>
<svg class="lawn-sign" viewBox="0 0 1618 1213" xmlns="http://www.w3.org/2000/svg" role="img" aria-label="Harlow Restoration Remodeling Group LLC lawn sign: roofing, gutters, windows">
  <defs>
    <linearGradient id="phone-bar-fill" x1="0" y1="0" x2="0" y2="1">
      <stop offset="0" stop-color="var(--bar-top)"/>
      <stop offset="1" stop-color="var(--bar-bottom)"/>
    </linearGradient>
    <filter id="number-shadow" x="-5%" y="-5%" width="110%" height="120%">
      <feDropShadow dx="4" dy="4" stdDeviation="2" flood-color="#0a1f45" flood-opacity="0.8"/>
    </filter>
  </defs>

  <rect class="sign-face" x="0" y="0" width="1618" height="1213"/>

  <g class="header-swoosh">
    <path class="band-leaf" d="M0 0 H1618 V222 Q700 -30 0 133 Z"/>
    <path class="band-forest" d="M958 0 H1618 V145 Q1300 55 958 0 Z"/>
    <path class="band-sky" d="M0 133 Q700 -30 1618 222 V237 Q700 10 0 195 Z"/>
  </g>

  <g class="company-name" text-anchor="end">
    <text x="1316" y="542" font-size="92">HARLOW</text>
    <text x="1316" y="632" font-size="66">RESTORATION</text>
    <text x="1316" y="707" font-size="66">REMODELING GROUP LLC</text>
  </g>

  <line class="divider" x1="260" y1="741" x2="1358" y2="741"/>

  <g class="services">
    <text class="service" x="158" y="875" textLength="347" lengthAdjust="spacingAndGlyphs">ROOFING</text>
    <text class="service" x="598" y="875" textLength="367" lengthAdjust="spacingAndGlyphs">GUTTERS</text>
    <text class="service" x="1061" y="875" textLength="399" lengthAdjust="spacingAndGlyphs">WINDOWS</text>
  </g>

  <g class="phone-bar">
    <rect x="0" y="907" width="1618" height="190" fill="url(#phone-bar-fill)"/>
    <circle class="phone-ring" cx="290" cy="997" r="68"/>
    <path class="phone-glyph" transform="translate(290 997) scale(4.2) translate(-12 -12)"
      d="M6.6 10.8c1.4 2.8 3.8 5.1 6.6 6.6l2.2-2.2c.3-.3.7-.4 1-.2 1.1.4 2.3.6 3.6.6.6 0 1 .4 1 1V20c0 .6-.4 1-1 1C10.6 21 3 13.4 3 4c0-.6.4-1 1-1h3.5c.6 0 1 .4 1 1 0 1.3.2 2.5.6 3.6.1.3 0 .7-.2 1L6.6 10.8z"/>
    <text class="phone-number" x="398" y="1069" textLength="993" lengthAdjust="spacingAndGlyphs" filter="url(#number-shadow)">555-014-2738</text>
  </g>

  <text class="website" x="493" y="1182" textLength="645" lengthAdjust="spacingAndGlyphs">WWW.HARLOWLLC.COM</text>
</svg>
</body>
</html>
```